social interest sharing site needs a web site design

we need a web site design for a social web platform.
the site is one page(main page), that is split into 3 sections
each section is a different color(red,green and blue)
and a user can choose to share each of the sections.
any section/color will contain boxes , each box can contain different media types.

the media types:
* list of URLS
* list of articles including title + image + description
* list of videos
* thumbnails of images
* calender
* list of emails

the main content will look like corkboardly layout
multiple boxes each box can contain different type of content as described above

each color is a different tab
each tab will have layout like corkboardly
Updates

please read the last description update.
and i uploaded an image that can explain the requirements better

thanks
Oren
 

Industry/Entity Type

Media

```html
<!DOCTYPE html>
<html lang="en">
<head>
<meta charset="utf-8">
<title>Tabora.me — Home Page</title>
<link rel="stylesheet" href="https://fonts.googleapis.com/css2?family=Open+Sans:wght@400;600;700;800&family=Montserrat:wght@400;700&display=swap">
<style>
:root{
  --coral:#f37b7b;
  --coral-dark:#e0625f;
  --green:#8cc63f;
  --teal:#2bb6d3;
  --ink:#2b2b2b;
  --header:#333537;
  --subtab:#3f4144;
  --card:#ffffff;
  --muted:#8a8a8a;
  --line:#e4e4e4;
  --video:#151515;
  --video-body:#1e1e1e;
  --cal-bg:#3a3c3f;
  --cal-cell:#d9d9d9;
  --cal-active:#2b8fd6;
  --orange:#f26b3a;
  --blue:#3c8fd6;
}
*{box-sizing:border-box;margin:0;padding:0}
html,body{width:1200px;height:3044px;overflow:hidden}
body{background:var(--coral);font-family:"Open Sans",Arial,sans-serif;color:var(--ink);position:relative}

/* header */
.site-header{position:absolute;left:0;top:0;width:1200px;height:56px;background:var(--header);display:flex;align-items:center;padding:0 32px}
.brand{font-family:"Montserrat",Arial,sans-serif;font-weight:700;font-size:30px;color:var(--coral);letter-spacing:-.5px;display:flex;align-items:center;gap:10px}
.brand-dot{width:14px;height:14px;background:var(--coral);display:inline-block}
.search{margin-left:auto;width:220px;height:28px;background:#4a4c4f;border-radius:3px;display:flex;align-items:center;justify-content:space-between;padding:0 10px;color:#cfcfcf;font-size:12px}
.social{display:flex;gap:8px;margin-left:22px}
.social span{width:26px;height:26px;border-radius:3px;display:block}
.social .s1{background:var(--orange)}.social .s2{background:var(--blue)}.social .s3{background:var(--teal)}
.auth{display:flex;gap:8px;margin-left:22px}
.btn{height:26px;padding:0 14px;border-radius:3px;font-size:11px;font-weight:700;color:#fff;display:flex;align-items:center;letter-spacing:.5px}
.btn-login{background:#5a5c5f}.btn-signup{background:var(--coral)}

/* tab row */
.tab-row{position:absolute;left:0;top:56px;width:1200px;height:94px;background:#fff;display:flex;align-items:flex-end;padding:0 32px 0}
.tab{height:78px;padding:14px 18px;color:#fff;display:flex;flex-direction:column;justify-content:flex-end;margin-right:6px}
.tab small{font-size:11px;opacity:.85;letter-spacing:1px}
.tab strong{font-family:"Montserrat",Arial,sans-serif;font-size:21px;font-weight:700;letter-spacing:.3px;line-height:1.1}
.tab-red{background:var(--coral);width:170px}
.tab-green{background:var(--green);width:214px}
.tab-blue{background:var(--teal);width:200px}
.following{font-size:13px;font-weight:700;line-height:1.25;color:var(--ink);align-self:center;margin:0 14px 0 14px;width:80px}
.subtabs{display:flex;gap:4px;height:78px}
.subtab{width:120px;background:var(--subtab);color:#e8e8e8;font-size:12px;font-weight:600;line-height:1.3;padding:14px 12px}
.subtab.active{background:#2a2b2d}

/* calendar */
.calendar{position:absolute;left:816px;top:132px;width:356px;height:232px;background:var(--cal-bg);padding:10px 12px;z-index:5;box-shadow:0 4px 10px rgba(0,0,0,.3)}
.cal-head{display:flex;justify-content:space-between;align-items:center;background:#fff;height:26px;padding:0 10px;font-size:13px;font-weight:700}
.cal-table{width:100%;border-collapse:separate;border-spacing:3px;margin-top:4px}
.cal-table th{color:#dcdcdc;font-size:11px;font-weight:600;height:20px}
.cal-table td{background:var(--cal-cell);font-size:11px;text-align:center;height:26px;color:#444}
.cal-table td.off{background:#777;color:#555}
.cal-table td.today{background:var(--cal-active);color:#fff;font-weight:700}

/* board */
.board{position:absolute;left:32px;top:170px;width:1140px;display:grid;grid-template-columns:repeat(3,356px);column-gap:36px;row-gap:28px}
.card{background:var(--card);height:366px;display:flex;flex-direction:column}
.card-media{height:236px;position:relative}
.card-body{padding:10px 10px 8px;display:flex;gap:8px;flex:1}
.card-text{flex:1}
.card-title{display:flex;align-items:center;gap:7px;font-size:13px;font-weight:600;margin-bottom:6px}
.share{width:14px;height:14px;background:var(--blue);border-radius:2px;flex:none}
.share.alt{background:var(--teal)}
.card-desc{font-size:11px;line-height:1.5;color:var(--muted)}
.card-actions{width:20px;display:flex;flex-direction:column;justify-content:space-between;align-items:center}
.card-actions svg{width:16px;height:16px}

.card.video{background:var(--video-body)}
.card.video .card-media{background:var(--video)}
.card.video .card-title{color:#ddd}
.card.video .card-desc{color:#888}
.play{position:absolute;left:50%;top:50%;width:64px;height:64px;margin:-38px 0 0 -32px;border-radius:50%;background:#fff;display:flex;align-items:center;justify-content:center}
.controls{position:absolute;left:0;right:0;bottom:0;height:22px;background:rgba(0,0,0,.75);display:flex;align-items:center;gap:8px;padding:0 8px}
.controls .bar{flex:1;height:4px;background:#555;position:relative}
.controls .bar i{position:absolute;left:0;top:0;height:4px;width:30%;background:var(--coral)}

/* footer */
.to-top{position:absolute;left:576px;top:2922px;width:48px;height:48px;border-radius:50%;background:#fff;display:flex;align-items:center;justify-content:center}
.site-footer{position:absolute;left:0;top:2996px;width:1200px;height:48px;background:var(--header);color:#bdbdbd;font-size:12px;display:flex;align-items:center;justify-content:center}
</style>
</head>
<body>

<header class="site-header">
  <div class="brand"><span class="brand-dot"></span>Tabora.me</div>
  <div class="search"><span>Search Form</span>
    <svg width="12" height="12" viewBox="0 0 12 12"><circle cx="5" cy="5" r="3.5" fill="none" stroke="#cfcfcf" stroke-width="1.5"/><line x1="7.6" y1="7.6" x2="11" y2="11" stroke="#cfcfcf" stroke-width="1.5"/></svg>
  </div>
  <div class="social"><span class="s1"></span><span class="s2"></span><span class="s3"></span></div>
  <div class="auth"><span class="btn btn-login">LOG IN</span><span class="btn btn-signup">SIGN UP</span></div>
</header>

<nav class="tab-row">
  <div class="tab tab-red"><small>RED</small><strong>HOME PAGE</strong></div>
  <div class="tab tab-green"><small>GREEN</small><strong>FAVORITES VIDEOS</strong></div>
  <div class="tab tab-blue"><small>BLUE</small><strong>PERSONAL APPS</strong></div>
  <div class="following">Following TABORA</div>
  <div class="subtabs">
    <div class="subtab">Jobs Favorites Videos</div>
    <div class="subtab active">Work Pics + Favorites Info</div>
    <div class="subtab">Family Weekly Calendar and notes</div>
  </div>
</nav>

<aside class="calendar">
  <div class="cal-head">
    <svg width="8" height="10" viewBox="0 0 8 10"><path d="M7 0 1 5l6 5z" fill="#333"/></svg>
    <span>January, 2014</span>
    <svg width="8" height="10" viewBox="0 0 8 10"><path d="M1 0l6 5-6 5z" fill="#333"/></svg>
  </div>
  <table class="cal-table">
    <tr><th>Sun</th><th>Mon</th><th>Tue</th><th>Wed</th><th>Thu</th><th>Fri</th><th>Sat</th></tr>
    <tr><td class="off">29</td><td class="off">30</td><td class="off">31</td><td>1</td><td>2</td><td>3</td><td>4</td></tr>
    <tr><td>5</td><td>6</td><td>7</td><td>8</td><td>9</td><td>10</td><td>11</td></tr>
    <tr><td>12</td><td>13</td><td>14</td><td>15</td><td>16</td><td class="today">17</td><td>18</td></tr>
    <tr><td>19</td><td>20</td><td>21</td><td>22</td><td>23</td><td>24</td><td>25</td></tr>
    <tr><td>26</td><td>27</td><td>28</td><td>29</td><td>30</td><td>31</td><td class="off">1</td></tr>
  </table>
</aside>

<main class="board">
  <!-- row 1 -->
  <article class="card"><div class="card-media" role="img" aria-label="Photo of a decorated Christmas tree beside a fireplace" style="background:linear-gradient(135deg,#6e2a1f,#b0573a)"></div>
    <div class="card-body"><div class="card-text"><div class="card-title"><span class="share"></span>Lorem ipsum is simply dummy</div><p class="card-desc">Lorem Ipsum is simply dummy text of the printing and typesetting industry. Lorem Ipsum has been the industry's standard dummy text ever since.</p></div>
    <div class="card-actions"><svg viewBox="0 0 16 16"><path d="M8 14 2 8a3.5 3.5 0 0 1 6-4 3.5 3.5 0 0 1 6 4z" fill="none" stroke="#555" stroke-width="1.5"/></svg><svg viewBox="0 0 16 16"><path d="M1 8s3-5 7-5 7 5 7 5-3 5-7 5-7-5-7-5z" fill="#555"/><circle cx="8" cy="8" r="2" fill="#fff"/></svg></div></div></article>
  <article class="card"><div class="card-media" role="img" aria-label="Photo of a family in Santa hats celebrating" style="background:linear-gradient(135deg,#3f7a3a,#c84a44)"></div>
    <div class="card-body"><div class="card-text"><div class="card-title"><span class="share alt"></span>Lorem ipsum is simply dummy</div><p class="card-desc">Lorem Ipsum is simply dummy text of the printing and typesetting industry. Lorem Ipsum has been the industry's standard dummy text ever since.</p></div>
    <div class="card-actions"><svg viewBox="0 0 16 16"><path d="M8 14 2 8a3.5 3.5 0 0 1 6-4 3.5 3.5 0 0 1 6 4z" fill="none" stroke="#555" stroke-width="1.5"/></svg><svg viewBox="0 0 16 16"><path d="M1 8s3-5 7-5 7 5 7 5-3 5-7 5-7-5-7-5z" fill="#555"/><circle cx="8" cy="8" r="2" fill="#fff"/></svg></div></div></article>
  <article class="card"><div class="card-media" role="img" aria-label="Photo of a family outdoors" style="background:linear-gradient(135deg,#7a9a5a,#b8c890)"></div>
    <div class="card-body"><div class="card-text"><div class="card-title"><span class="share"></span>Lorem ipsum is simply dummy</div><p class="card-desc">Lorem Ipsum is simply dummy text of the printing and typesetting industry. Lorem Ipsum has been the industry's standard dummy text ever since.</p></div>
    <div class="card-actions"><svg viewBox="0 0 16 16"><path d="M8 1l2.2 4.5 4.8.7-3.5 3.4.8 4.9L8 12.2 3.7 14.5l.8-4.9L1 6.2l4.8-.7z" fill="none" stroke="#555" stroke-width="1.3"/></svg><svg viewBox="0 0 16 16"><path d="M1 8s3-5 7-5 7 5 7 5-3 5-7 5-7-5-7-5z" fill="#555"/><circle cx="8" cy="8" r="2" fill="#fff"/></svg></div></div></article>

  <!-- row 2 -->
  <article class="card"><div class="card-media" role="img" aria-label="Photo of friends playing in the snow" style="background:linear-gradient(135deg,#4d86c4,#d6e6f2)"></div>
    <div class="card-body"><div class="card-text"><div class="card-title"><span class="share"></span>Lorem ipsum is simply dummy</div><p class="card-desc">Lorem Ipsum is simply dummy text of the printing and typesetting industry. Lorem Ipsum has been the industry's standard dummy text ever since.</p></div>
    <div class="card-actions"><svg viewBox="0 0 16 16"><path d="M8 1l2.2 4.5 4.8.7-3.5 3.4.8 4.9L8 12.2 3.7 14.5l.8-4.9L1 6.2l4.8-.7z" fill="none" stroke="#555" stroke-width="1.3"/></svg><svg viewBox="0 0 16 16"><path d="M1 8s3-5 7-5 7 5 7 5-3 5-7 5-7-5-7-5z" fill="#555"/><circle cx="8" cy="8" r="2" fill="#fff"/></svg></div></div></article>
  <article class="card"><div class="card-media" role="img" aria-label="Photo of a smiling family together" style="background:linear-gradient(135deg,#a8876c,#e4d4c2)"></div>
    <div class="card-body"><div class="card-text"><div class="card-title"><span class="share alt"></span>Lorem ipsum is simply dummy</div><p class="card-desc">Lorem Ipsum is simply dummy text of the printing and typesetting industry. Lorem Ipsum has been the industry's standard dummy text ever since.</p></div>
    <div class="card-actions"><svg viewBox="0 0 16 16"><path d="M8 14 2 8a3.5 3.5 0 0 1 6-4 3.5 3.5 0 0 1 6 4z" fill="none" stroke="#555" stroke-width="1.5"/></svg><svg viewBox="0 0 16 16"><path d="M1 8s3-5 7-5 7 5 7 5-3 5-7 5-7-5-7-5z" fill="#555"/><circle cx="8" cy="8" r="2" fill="#fff"/></svg></div></div></article>
  <article class="card"><div class="card-media" role="img" aria-label="Video still of children lying on green grass" style="background:linear-gradient(135deg,#5f9a2e,#a8d06a)"><div class="controls"><svg width="8" height="10" viewBox="0 0 8 10"><path d="M0 0l8 5-8 5z" fill="#fff"/></svg><span class="bar"><i></i></span></div></div>
    <div class="card-body"><div class="card-text"><div class="card-title"><span class="share"></span>Lorem ipsum is simply dummy</div><p class="card-desc">Lorem Ipsum is simply dummy text of the printing and typesetting industry. Lorem Ipsum has been the industry's standard dummy text ever since.</p></div>
    <div class="card-actions"><svg viewBox="0 0 16 16"><path d="M8 14 2 8a3.5 3.5 0 0 1 6-4 3.5 3.5 0 0 1 6 4z" fill="none" stroke="#555" stroke-width="1.5"/></svg><svg viewBox="0 0 16 16"><path d="M1 8s3-5 7-5 7 5 7 5-3 5-7 5-7-5-7-5z" fill="#555"/><circle cx="8" cy="8" r="2" fill="#fff"/></svg></div></div></article>

  <!-- row 3 -->
  <article class="card"><div class="card-media" role="img" aria-label="Photo of green smoothies with limes" style="background:linear-gradient(135deg,#7fae2c,#d4e69a)"></div>
    <div class="card-body"><div class="card-text"><div class="card-title"><span class="share"></span>Lorem ipsum is simply dummy</div><p class="card-desc">Lorem Ipsum is simply dummy text of the printing and typesetting industry. Lorem Ipsum has been the industry's standard dummy text ever since.</p></div>
    <div class="card-actions"><svg viewBox="0 0 16 16"><path d="M8 1l2.2 4.5 4.8.7-3.5 3.4.8 4.9L8 12.2 3.7 14.5l.8-4.9L1 6.2l4.8-.7z" fill="none" stroke="#555" stroke-width="1.3"/></svg><svg viewBox="0 0 16 16"><path d="M1 8s3-5 7-5 7 5 7 5-3 5-7 5-7-5-7-5z" fill="#555"/><circle cx="8" cy="8" r="2" fill="#fff"/></svg></div></div></article>
  <article class="card"><div class="card-media" role="img" aria-label="Photo of a family holding holiday gifts" style="background:linear-gradient(135deg,#8c3a30,#d88a6a)"></div>
    <div class="card-body"><div class="card-text"><div class="card-title"><span class="share alt"></span>Lorem ipsum is simply dummy</div><p class="card-desc">Lorem Ipsum is simply dummy text of the printing and typesetting industry. Lorem Ipsum has been the industry's standard dummy text ever since.</p></div>
    <div class="card-actions"><svg viewBox="0 0 16 16"><path d="M8 14 2 8a3.5 3.5 0 0 1 6-4 3.5 3.5 0 0 1 6 4z" fill="none" stroke="#555" stroke-width="1.5"/></svg><svg viewBox="0 0 16 16"><path d="M1 8s3-5 7-5 7 5 7 5-3 5-7 5-7-5-7-5z" fill="#555"/><circle cx="8" cy="8" r="2" fill="#fff"/></svg></div></div></article>
  <article class="card video"><div class="card-media"><span class="play"><svg width="22" height="26" viewBox="0 0 22 26"><path d="M2 1l19 12L2 25z" fill="#151515"/></svg></span><div class="controls"><svg width="8" height="10" viewBox="0 0 8 10"><path d="M0 0l8 5-8 5z" fill="#fff"/></svg><span class="bar"><i></i></span></div></div>
    <div class="card-body"><div class="card-text"><div class="card-title"><span class="share"></span>Lorem ipsum is simply dummy</div><p class="card-desc">Lorem Ipsum is simply dummy text of the printing and typesetting industry. Lorem Ipsum has been the industry's standard dummy text ever since.</p></div>
    <div class="card-actions"><svg viewBox="0 0 16 16"><path d="M8 14 2 8a3.5 3.5 0 0 1 6-4 3.5 3.5 0 0 1 6 4z" fill="none" stroke="#aaa" stroke-width="1.5"/></svg><svg viewBox="0 0 16 16"><path d="M1 8s3-5 7-5 7 5 7 5-3 5-7 5-7-5-7-5z" fill="#aaa"/><circle cx="8" cy="8" r="2" fill="#1e1e1e"/></svg></div></div></article>

  <!-- row 4 -->
  <article class="card"><div class="card-media" role="img" aria-label="Photo of a woman working on a laptop" style="background:linear-gradient(135deg,#cfc6bc,#f0ece6)"></div>
    <div class="card-body"><div class="card-text"><div class="card-title"><span class="share"></span>Lorem ipsum is simply dummy</div><p class="card-desc">Lorem Ipsum is simply dummy text of the printing and typesetting industry. Lorem Ipsum has been the industry's standard dummy text ever since.</p></div>
    <div class="card-actions"><svg viewBox="0 0 16 16"><path d="M8 14 2 8a3.5 3.5 0 0 1 6-4 3.5 3.5 0 0 1 6 4z" fill="none" stroke="#555" stroke-width="1.5"/></svg><svg viewBox="0 0 16 16"><path d="M1 8s3-5 7-5 7 5 7 5-3 5-7 5-7-5-7-5z" fill="#555"/><circle cx="8" cy="8" r="2" fill="#fff"/></svg></div></div></article>
  <article class="card"><div class="card-media" role="img" aria-label="Photo of a covered patio with garden furniture" style="background:linear-gradient(135deg,#8a7258,#d2c2a6)"></div>
    <div class="card-body"><div class="card-text"><div class="card-title"><span class="share alt"></span>Lorem ipsum is simply dummy</div><p class="card-desc">Lorem Ipsum is simply dummy text of the printing and typesetting industry. Lorem Ipsum has been the industry's standard dummy text ever since.</p></div>
    <div class="card-actions"><svg viewBox="0 0 16 16"><path d="M8 1l2.2 4.5 4.8.7-3.5 3.4.8 4.9L8 12.2 3.7 14.5l.8-4.9L1 6.2l4.8-.7z" fill="none" stroke="#555" stroke-width="1.3"/></svg><svg viewBox="0 0 16 16"><path d="M1 8s3-5 7-5 7 5 7 5-3 5-7 5-7-5-7-5z" fill="#555"/><circle cx="8" cy="8" r="2" fill="#fff"/></svg></div></div></article>
  <article class="card"><div class="card-media" role="img" aria-label="Photo of children playing in the snow" style="background:linear-gradient(135deg,#8ea6c0,#e4ecf4)"></div>
    <div class="card-body"><div class="card-text"><div class="card-title"><span class="share"></span>Lorem ipsum is simply dummy</div><p class="card-desc">Lorem Ipsum is simply dummy text of the printing and typesetting industry. Lorem Ipsum has been the industry's standard dummy text ever since.</p></div>
    <div class="card-actions"><svg viewBox="0 0 16 16"><path d="M8 14 2 8a3.5 3.5 0 0 1 6-4 3.5 3.5 0 0 1 6 4z" fill="none" stroke="#555" stroke-width="1.5"/></svg><svg viewBox="0 0 16 16"><path d="M1 8s3-5 7-5 7 5 7 5-3 5-7 5-7-5-7-5z" fill="#555"/><circle cx="8" cy="8" r="2" fill="#fff"/></svg></div></div></article>

  <!-- row 5 -->
  <article class="card"><div class="card-media" role="img" aria-label="Photo of a suburban house with a front lawn" style="background:linear-gradient(180deg,#7fa2c8,#9aa48a)"></div>
    <div class="card-body"><div class="card-text"><div class="card-title"><span class="share"></span>Lorem ipsum is simply dummy</div><p class="card-desc">Lorem Ipsum is simply dummy text of the printing and typesetting industry. Lorem Ipsum has been the industry's standard dummy text ever since.</p></div>
    <div class="card-actions"><svg viewBox="0 0 16 16"><path d="M8 1l2.2 4.5 4.8.7-3.5 3.4.8 4.9L8 12.2 3.7 14.5l.8-4.9L1 6.2l4.8-.7z" fill="none" stroke="#555" stroke-width="1.3"/></svg><svg viewBox="0 0 16 16"><path d="M1 8s3-5 7-5 7 5 7 5-3 5-7 5-7-5-7-5z" fill="#555"/><circle cx="8" cy="8" r="2" fill="#fff"/></svg></div></div></article>
  <article class="card"><div class="card-media" role="img" aria-label="Photo of a baby in a knitted hat" style="background:linear-gradient(135deg,#c8b6a6,#efe6de)"></div>
    <div class="card-body"><div class="card-text"><div class="card-title"><span class="share alt"></span>Lorem ipsum is simply dummy</div><p class="card-desc">Lorem Ipsum is simply dummy text of the printing and typesetting industry. Lorem Ipsum has been the industry's standard dummy text ever since.</p></div>
    <div class="card-actions"><svg viewBox="0 0 16 16"><path d="M8 14 2 8a3.5 3.5 0 0 1 6-4 3.5 3.5 0 0 1 6 4z" fill="none" stroke="#555" stroke-width="1.5"/></svg><svg viewBox="0 0 16 16"><path d="M1 8s3-5 7-5 7 5 7 5-3 5-7 5-7-5-7-5z" fill="#555"/><circle cx="8" cy="8" r="2" fill="#fff"/></svg></div></div></article>
  <article class="card video"><div class="card-media"><span class="play"><svg width="22" height="26" viewBox="0 0 22 26"><path d="M2 1l19 12L2 25z" fill="#151515"/></svg></span><div class="controls"><svg width="8" height="10" viewBox="0 0 8 10"><path d="M0 0l8 5-8 5z" fill="#fff"/></svg><span class="bar"><i></i></span></div></div>
    <div class="card-body"><div class="card-text"><div class="card-title"><span class="share"></span>Lorem ipsum is simply dummy</div><p class="card-desc">Lorem Ipsum is simply dummy text of the printing and typesetting industry. Lorem Ipsum has been the industry's standard dummy text ever since.</p></div>
    <div class="card-actions"><svg viewBox="0 0 16 16"><path d="M8 1l2.2 4.5 4.8.7-3.5 3.4.8 4.9L8 12.2 3.7 14.5l.8-4.9L1 6.2l4.8-.7z" fill="none" stroke="#aaa" stroke-width="1.3"/></svg><svg viewBox="0 0 16 16"><path d="M1 8s3-5 7-5 7 5 7 5-3 5-7 5-7-5-7-5z" fill="#aaa"/><circle cx="8" cy="8" r="2" fill="#1e1e1e"/></svg></div></div></article>

  <!-- row 6 -->
  <article class="card"><div class="card-media" role="img" aria-label="Photo of a bright dining room" style="background:linear-gradient(135deg,#b88a66,#e8d8c4)"></div>
    <div class="card-body"><div class="card-text"><div class="card-title"><span class="share"></span>Lorem ipsum is simply dummy</div><p class="card-desc">Lorem Ipsum is simply dummy text of the printing and typesetting industry. Lorem Ipsum has been the industry's standard dummy text ever since.</p></div>
    <div class="card-actions"><svg viewBox="0 0 16 16"><path d="M8 14 2 8a3.5 3.5 0 0 1 6-4 3.5 3.5 0 0 1 6 4z" fill="none" stroke="#555" stroke-width="1.5"/></svg><svg viewBox="0 0 16 16"><path d="M1 8s3-5 7-5 7 5 7 5-3 5-7 5-7-5-7-5z" fill="#555"/><circle cx="8" cy="8" r="2" fill="#fff"/></svg></div></div></article>
  <article class="card"><div class="card-media" role="img" aria-label="Photo of a breakfast of cereal, fruit and milk" style="background:linear-gradient(135deg,#d8b860,#f2eee0)"></div>
    <div class="card-body"><div class="card-text"><div class="card-title"><span class="share alt"></span>Lorem ipsum is simply dummy</div><p class="card-desc">Lorem Ipsum is simply dummy text of the printing and typesetting industry. Lorem Ipsum has been the industry's standard dummy text ever since.</p></div>
    <div class="card-actions"><svg viewBox="0 0 16 16"><path d="M8 1l2.2 4.5 4.8.7-3.5 3.4.8 4.9L8 12.2 3.7 14.5l.8-4.9L1 6.2l4.8-.7z" fill="none" stroke="#555" stroke-width="1.3"/></svg><svg viewBox="0 0 16 16"><path d="M1 8s3-5 7-5 7 5 7 5-3 5-7 5-7-5-7-5z" fill="#555"/><circle cx="8" cy="8" r="2" fill="#fff"/></svg></div></div></article>
  <article class="card"><div class="card-media" role="img" aria-label="Photo of a couple embracing" style="background:linear-gradient(135deg,#b88c70,#e8d4c2)"></div>
    <div class="card-body"><div class="card-text"><div class="card-title"><span class="share"></span>Lorem ipsum is simply dummy</div><p class="card-desc">Lorem Ipsum is simply dummy text of the printing and typesetting industry. Lorem Ipsum has been the industry's standard dummy text ever since.</p></div>
    <div class="card-actions"><svg viewBox="0 0 16 16"><path d="M8 14 2 8a3.5 3.5 0 0 1 6-4 3.5 3.5 0 0 1 6 4z" fill="none" stroke="#555" stroke-width="1.5"/></svg><svg viewBox="0 0 16 16"><path d="M1 8s3-5 7-5 7 5 7 5-3 5-7 5-7-5-7-5z" fill="#555"/><circle cx="8" cy="8" r="2" fill="#fff"/></svg></div></div></article>

  <!-- row 7 -->
  <article class="card"><div class="card-media" role="img" aria-label="Photo of a woman sitting outdoors" style="background:linear-gradient(135deg,#8ea656,#e2e8c8)"></div>
    <div class="card-body"><div class="card-text"><div class="card-title"><span class="share"></span>Lorem ipsum is simply dummy</div><p class="card-desc">Lorem Ipsum is simply dummy text of the printing and typesetting industry. Lorem Ipsum has been the industry's standard dummy text ever since.</p></div>
    <div class="card-actions"><svg viewBox="0 0 16 16"><path d="M8 1l2.2 4.5 4.8.7-3.5 3.4.8 4.9L8 12.2 3.7 14.5l.8-4.9L1 6.2l4.8-.7z" fill="none" stroke="#555" stroke-width="1.3"/></svg><svg viewBox="0 0 16 16"><path d="M1 8s3-5 7-5 7 5 7 5-3 5-7 5-7-5-7-5z" fill="#555"/><circle cx="8" cy="8" r="2" fill="#fff"/></svg></div></div></article>
  <article class="card"><div class="card-media" role="img" aria-label="Photo of a man with a laptop" style="background:linear-gradient(135deg,#c8ccd0,#f4f4f2)"></div>
    <div class="card-body"><div class="card-text"><div class="card-title"><span class="share alt"></span>Lorem ipsum is simply dummy</div><p class="card-desc">Lorem Ipsum is simply dummy text of the printing and typesetting industry. Lorem Ipsum has been the industry's standard dummy text ever since.</p></div>
    <div class="card-actions"><svg viewBox="0 0 16 16"><path d="M8 14 2 8a3.5 3.5 0 0 1 6-4 3.5 3.5 0 0 1 6 4z" fill="none" stroke="#555" stroke-width="1.5"/></svg><svg viewBox="0 0 16 16"><path d="M1 8s3-5 7-5 7 5 7 5-3 5-7 5-7-5-7-5z" fill="#555"/><circle cx="8" cy="8" r="2" fill="#fff"/></svg></div></div></article>
  <article class="card video"><div class="card-media"><span class="play"><svg width="22" height="26" viewBox="0 0 22 26"><path d="M2 1l19 12L2 25z" fill="#151515"/></svg></span><div class="controls"><svg width="8" height="10" viewBox="0 0 8 10"><path d="M0 0l8 5-8 5z" fill="#fff"/></svg><span class="bar"><i></i></span></div></div>
    <div class="card-body"><div class="card-text"><div class="card-title"><span class="share"></span>Lorem ipsum is simply dummy</div><p class="card-desc">Lorem Ipsum is simply dummy text of the printing and typesetting industry. Lorem Ipsum has been the industry's standard dummy text ever since.</p></div>
    <div class="card-actions"><svg viewBox="0 0 16 16"><path d="M8 14 2 8a3.5 3.5 0 0 1 6-4 3.5 3.5 0 0 1 6 4z" fill="none" stroke="#aaa" stroke-width="1.5"/></svg><svg viewBox="0 0 16 16"><path d="M1 8s3-5 7-5 7 5 7 5-3 5-7 5-7-5-7-5z" fill="#aaa"/><circle cx="8" cy="8" r="2" fill="#1e1e1e"/></svg></div></div></article>
</main>

<div class="to-top"><svg width="20" height="14" viewBox="0 0 20 14"><path d="M2 12l8-8 8 8" fill="none" stroke="var(--coral)" stroke-width="3"/></svg></div>

<footer class="site-footer">Copyright © 2013 Tabora.me. All rights reserved.</footer>

</body>
</html>
```